Business card, postcard, pocket folder

We are a real estate team and have had a new logo designed. From this, we need the following deliverables:- Business Cards (double-sided)- Just Listed / Just Sold Postcards (double-sided)- Pocket Folder. See logo attached.More work possible for the winning designer.
There are 5 members of the team, so head shots should be easily changed and possible for a group photo might be a good idea for the pocket folder but not 100% neccessary.
Target Market(s)
Real estate
Industry/Entity Type
Real Estate
Font styles to use
Serif
Sans Serif
Requirements
Must have
- Business cards and postcards must have a head shot on them.

```html
<!DOCTYPE html>
<html lang="en">
<head>
<meta charset="utf-8">
<title>Harbourline Group – Stationery Set</title>
<link rel="stylesheet" href="https://fonts.googleapis.com/css2?family=Open+Sans:wght@400;600;700&display=swap">
<style>
  :root{
    --blue:#2a3b92;
    --red:#d9202b;
    --white:#ffffff;
    --ink:#2b2b2b;
    --bg:#d2d2d2;
    --photo-sky:#a9c6e6;
    --photo-house:#d9dde2;
    --photo-warm:#8a6a52;
    --photo-suit:#3a4054;
  }
  *{box-sizing:border-box;margin:0;padding:0}
  html,body{width:1200px;height:953px;overflow:hidden}
  body{background:var(--bg);font-family:"Open Sans",Arial,sans-serif;color:var(--ink);position:relative}
  .piece{position:absolute;background:var(--white);overflow:hidden;box-shadow:0 3px 8px rgba(0,0,0,.18)}
  .brand-name{font-family:"Open Sans",Arial,sans-serif;font-weight:700;color:var(--blue);white-space:nowrap}
  .brand-name.on-dark{color:var(--white)}
  .band{position:absolute;left:0;right:0;bottom:0;background:var(--blue)}
  .icon{width:9px;height:9px;fill:var(--red);flex:none}
  .contact-list{list-style:none;display:flex;flex-direction:column;gap:3px}
  .contact-list li{display:flex;align-items:center;gap:6px;white-space:nowrap}

  /* Postcard front */
  .postcard{width:440px;height:240px}
  .postcard .photo{position:absolute;right:0;top:0;width:56%;height:100%;
    background:linear-gradient(180deg,var(--photo-sky) 0%,var(--photo-house) 55%,var(--photo-warm) 100%)}
  .postcard .price{position:absolute;left:0;top:42px;width:190px;height:38px;background:var(--red);color:var(--white);
    font-weight:600;font-size:20px;line-height:38px;padding-left:14px}
  .postcard .tag{position:absolute;left:194px;top:42px;width:90px;height:20px;background:var(--blue);color:var(--white);
    font-size:10px;font-weight:600;line-height:20px;text-align:center;letter-spacing:.5px}
  .postcard .copy{position:absolute;left:14px;top:92px;width:170px;font-size:8px;line-height:1.35}
  .postcard-front .contact-list{position:absolute;left:14px;top:160px;font-size:8px}
  .postcard .band{height:26px;clip-path:polygon(0 100%,100% 0,100% 100%)}

  /* Postcard back */
  .postcard-back .photo{position:absolute;left:0;top:0;width:55%;height:100%;
    background:linear-gradient(160deg,#c9a77c 0%,#8b7a6a 45%,var(--photo-suit) 100%)}
  .postcard-back .side{position:absolute;left:58%;top:36px;right:10px;z-index:1}
  .postcard-back .brand-name{font-size:15px;margin-bottom:16px}
  .postcard-back .contact-list{font-size:9px;gap:5px}
  .postcard-back .band{left:55%;height:70px;clip-path:polygon(0 60%,100% 0,100% 100%,0 100%)}

  /* Business cards */
  .card{width:210px;height:120px}
  .card .photo{position:absolute;left:0;top:0;width:44%;height:100%;
    background:linear-gradient(180deg,#eceae6 0%,#b9b4ad 50%,var(--photo-suit) 100%)}
  .card .name-tag{position:absolute;left:44%;top:14px;width:78px;height:18px;background:var(--red);color:var(--white);
    font-size:9px;font-weight:600;line-height:18px;padding-left:6px}
  .card .role{position:absolute;left:calc(44% + 6px);top:34px;font-size:5px;color:var(--red);font-weight:600}
  .card .contact-list{position:absolute;left:calc(44% + 6px);top:44px;font-size:5px;gap:2px}
  .card .icon{width:5px;height:5px}
  .card .band{left:44%;height:30px;clip-path:polygon(0 70%,100% 0,100% 100%,0 100%)}
  .card-back{width:210px;height:120px;background:var(--blue);display:flex;align-items:center;justify-content:center}
  .card-back .brand-name{font-size:13px}

  /* Letterhead */
  .letterhead{width:300px;height:420px}
  .letterhead .brand-name{position:absolute;top:26px;width:100%;text-align:center;font-size:12px}
  .letterhead .band{height:70px;clip-path:polygon(0 88%,100% 40%,100% 100%,0 100%)}
  .letterhead .footer{position:absolute;left:14px;bottom:26px;display:flex;flex-direction:column;gap:2px;
    font-size:5px;color:var(--blue);z-index:1}
  .letterhead .footer span{display:flex;align-items:center;gap:3px;white-space:nowrap}
  .letterhead .footer .icon{width:5px;height:5px;fill:var(--blue)}

  /* Folder */
  .folder{width:340px;height:480px;background:var(--blue)}
  .folder .brand-name{position:absolute;top:120px;width:100%;text-align:center;font-size:22px}
  .folder .band{height:90px;background:var(--red);clip-path:polygon(0 92%,100% 30%,100% 100%,0 100%)}
  .folder .web{position:absolute;left:30px;bottom:46px;color:var(--white);font-size:11px}
</style>
</head>
<body>
<svg width="0" height="0" style="position:absolute" aria-hidden="true">
  <symbol id="i-pin" viewBox="0 0 10 10"><path d="M5 0a3.5 3.5 0 0 0-3.5 3.5C1.5 6 5 10 5 10s3.5-4 3.5-6.5A3.5 3.5 0 0 0 5 0zm0 5a1.5 1.5 0 1 1 0-3 1.5 1.5 0 0 1 0 3z"/></symbol>
  <symbol id="i-phone" viewBox="0 0 10 10"><path d="M2 0h6v10H2zM3 1v7h4V1z"/></symbol>
  <symbol id="i-mail" viewBox="0 0 10 10"><path d="M0 2h10v6H0zm1 1v.4l4 2.6 4-2.6V3z"/></symbol>
  <symbol id="i-web" viewBox="0 0 10 10"><path d="M5 0a5 5 0 1 0 0 10A5 5 0 0 0 5 0zm0 1.5a3.5 3.5 0 1 1 0 7 3.5 3.5 0 0 1 0-7z"/></symbol>
</svg>

<!-- Postcard front -->
<section class="piece postcard postcard-front" style="left:30px;top:40px">
  <div class="photo" role="img" aria-label="Photo of a modern white two-storey house under blue sky"></div>
  <div class="price">$399 000</div>
  <div class="tag">JUST LISTED</div>
  <p class="copy">Lorem ipsum dolor sit amet, consectetuer adipiscing elit, sed diam. Lorem ipsum dolor sit amet, consectetuer adipiscing elit, sed diam. Lorem ipsum dolor sit amet, consectetuer adipiscing elit, sed diam.</p>
  <ul class="contact-list">
    <li><svg class="icon"><use href="#i-pin"/></svg>1280 Maple Row, Lakeview H2B 4T7</li>
    <li><svg class="icon"><use href="#i-phone"/></svg>555-301-2284</li>
    <li><svg class="icon"><use href="#i-mail"/></svg>nora@harbourlinegroup.ca</li>
    <li><svg class="icon"><use href="#i-web"/></svg>harbourlinegroup.ca</li>
  </ul>
  <div class="band"></div>
</section>

<!-- Postcard back -->
<section class="piece postcard postcard-back" style="left:30px;top:300px">
  <div class="photo" role="img" aria-label="Group photo of the five-person real estate team"></div>
  <div class="band"></div>
  <div class="side">
    <div class="brand-name">Harbourline Group</div>
    <ul class="contact-list">
      <li><svg class="icon"><use href="#i-pin"/></svg>1280 Maple Row, Lakeview H2B 4T7</li>
      <li><svg class="icon"><use href="#i-phone"/></svg>555-301-2284</li>
      <li><svg class="icon"><use href="#i-mail"/></svg>nora@harbourlinegroup.ca</li>
      <li><svg class="icon"><use href="#i-web"/></svg>harbourlinegroup.ca</li>
    </ul>
  </div>
</section>

<!-- Business cards -->
<section class="piece card-back" style="left:30px;top:570px"><span class="brand-name on-dark">Harbourline Group</span></section>
<section class="piece card" style="left:260px;top:570px">
  <div class="photo" role="img" aria-label="Head shot of the realtor"></div>
  <div class="name-tag">Nora T Bell</div>
  <div class="role">REALTOR</div>
  <ul class="contact-list">
    <li><svg class="icon"><use href="#i-pin"/></svg>1280 Maple Row, Lakeview H2B 4T7</li>
    <li><svg class="icon"><use href="#i-phone"/></svg>555-301-2284</li>
    <li><svg class="icon"><use href="#i-mail"/></svg>nora@harbourlinegroup.ca</li>
    <li><svg class="icon"><use href="#i-web"/></svg>harbourlinegroup.ca</li>
  </ul>
  <div class="band"></div>
</section>
<section class="piece card" style="left:30px;top:710px">
  <div class="photo" role="img" aria-label="Head shot of the realtor"></div>
  <div class="name-tag">Nora T Bell</div>
  <div class="role">REALTOR</div>
  <ul class="contact-list">
    <li><svg class="icon"><use href="#i-pin"/></svg>1280 Maple Row, Lakeview H2B 4T7</li>
    <li><svg class="icon"><use href="#i-phone"/></svg>555-301-2284</li>
    <li><svg class="icon"><use href="#i-mail"/></svg>nora@harbourlinegroup.ca</li>
    <li><svg class="icon"><use href="#i-web"/></svg>harbourlinegroup.ca</li>
  </ul>
  <div class="band"></div>
</section>
<section class="piece card-back" style="left:260px;top:710px"><span class="brand-name on-dark">Harbourline Group</span></section>

<!-- Letterhead -->
<section class="piece letterhead" style="left:500px;top:40px">
  <div class="brand-name">Harbourline Group</div>
  <div class="band"></div>
  <div class="footer">
    <span><svg class="icon"><use href="#i-pin"/></svg>1280 Maple Row, Lakeview H2B 4T7</span>
    <span><svg class="icon"><use href="#i-phone"/></svg>555-301-2284</span>
    <span><svg class="icon"><use href="#i-mail"/></svg>nora@harbourlinegroup.ca</span>
  </div>
</section>

<!-- Pocket folder -->
<section class="piece folder" style="left:830px;top:40px">
  <div class="brand-name on-dark">Harbourline Group</div>
  <div class="web">harbourlinegroup.ca</div>
  <div class="band"></div>
</section>

<!-- Postcard front (second) -->
<section class="piece postcard postcard-front" style="left:500px;top:560px">
  <div class="photo" role="img" aria-label="Photo of a modern white two-storey house under blue sky"></div>
  <div class="price">$399 000</div>
  <div class="tag">JUST LISTED</div>
  <p class="copy">Lorem ipsum dolor sit amet, consectetuer adipiscing elit, sed diam. Lorem ipsum dolor sit amet, consectetuer adipiscing elit, sed diam. Lorem ipsum dolor sit amet, consectetuer adipiscing elit, sed diam.</p>
  <ul class="contact-list">
    <li><svg class="icon"><use href="#i-pin"/></svg>1280 Maple Row, Lakeview H2B 4T7</li>
    <li><svg class="icon"><use href="#i-phone"/></svg>555-301-2284</li>
    <li><svg class="icon"><use href="#i-mail"/></svg>nora@harbourlinegroup.ca</li>
    <li><svg class="icon"><use href="#i-web"/></svg>harbourlinegroup.ca</li>
  </ul>
  <div class="band"></div>
</section>
</body>
</html>
```